Locksmiths Business Card Designs needed!!

I need a business card design for my new small locksmith business.
I would love my business card to be simple, (not too many photos of locks or keys) but strong images so that everyone can recognise it is locksmithing business without reading the words.

I want all information i put in upper article to appear on front side in anyway depending on your design of suggestions and on the back side I would love to mention theses;
-24 /7 mobile services (including weekends & public holidays)
-Residential / Commercial/ Automotive
-Opening / Repair / Installation
-Cut keys

Im not a native english speaker so you can fix the words or expressions as you think it is right and natural.

I realised that in the business names, there is too many "locks" and "s" so I would love to seperate the words somehow so that it is more natural when someone read the business name on the card. for example,put the part of "Bright Harbor Access" first line and the part of "Locksmiths" on the other line....I am just suggesting..doesn't need to be like that..but it should say "Locksmiths" as it is locksmiths business. :)

Target Market(s)

all generations

Industry/Entity Type

Locksmith

Contact Information for Business Card

business name : Bright Harbor Access Services
ABN 41862093715
Name : Dean Rowe (푸른 문지기)
phone : 0468 219 357
email : brightharboraccess@mailverte.net

Requirements
Must have
• A symbol of either a key or a lock
Nice to have
• I like the symbol of a key in the photo I have attached here. So maybe, if you couldn't find any other good symbols I am happy to have the symbol on the business somehow.
Should not have
• Too many keys or locks

```html
<!DOCTYPE html>
<html lang="en">
<head>
<meta charset="utf-8">
<title>Bright Harbor Access Locksmiths – Business Card</title>
<link rel="stylesheet" href="https://fonts.googleapis.com/css2?family=Arimo:wght@400;700&family=Noto+Sans+KR:wght@700&display=swap">
<style>
  :root {
    --page: #ffffff;
    --card-dark: #3b3b39;
    --card-light: #ffffff;
    --ink-light: #f2f2f2;
    --ink-muted: #d9d9d6;
    --ink-dark: #111111;
    --key-tone: #c9c0a9;
    --edge: #bdbdbd;
  }
  * { margin: 0; padding: 0; box-sizing: border-box; }
  html, body {
    width: 1200px;
    height: 370px;
    overflow: hidden;
    background: var(--page);
    font-family: "Arimo", Arial, sans-serif;
  }
  .canvas {
    position: relative;
    width: 1200px;
    height: 370px;
  }
  .card {
    position: absolute;
    top: 15px;
    width: 572px;
    height: 340px;
    box-shadow: 1px 1px 3px var(--edge);
    overflow: hidden;
  }
  /* Front */
  .card-front {
    left: 18px;
    background: var(--card-dark);
  }
  .key-symbol {
    position: absolute;
    left: 168px;
    top: 45px;
    width: 290px;
    height: 175px;
  }
  .brand {
    position: absolute;
    left: 0;
    right: 0;
    top: 232px;
    text-align: center;
    color: var(--ink-light);
  }
  .brand-name {
    font-size: 22px;
    letter-spacing: 1px;
    text-transform: uppercase;
  }
  .brand-trade {
    margin-top: 14px;
    font-size: 22px;
    letter-spacing: 9px;
    text-transform: uppercase;
    padding-left: 9px;
  }
  /* Back */
  .card-back {
    left: 610px;
    background: var(--card-dark);
  }
  .contact {
    position: absolute;
    left: 0;
    top: 0;
    width: 100%;
    height: 142px;
    background: var(--card-light);
    padding: 20px 18px 0 0;
    text-align: right;
    color: var(--ink-dark);
    font-size: 19px;
    line-height: 25px;
  }
  .contact-name {
    font-weight: 700;
    font-size: 22px;
    line-height: 28px;
  }
  .contact-name .korean {
    font-family: "Noto Sans KR", Arial, sans-serif;
    font-size: 20px;
  }
  .services {
    position: absolute;
    left: 22px;
    top: 200px;
    list-style: none;
    color: var(--ink-muted);
    font-size: 18px;
    line-height: 27px;
  }
  .services li {
    position: relative;
    padding-left: 15px;
  }
  .services li::before {
    content: "";
    position: absolute;
    left: 0;
    top: 11px;
    width: 5px;
    height: 5px;
    background: var(--ink-muted);
  }
</style>
</head>
<body>
<div class="canvas">
  <section class="card card-front">
    <svg class="key-symbol" viewBox="0 0 290 175" role="img" aria-label="Ornate antique key illustration">
      <defs>
        <linearGradient id="keyGlow" x1="0" y1="1" x2="1" y2="0">
          <stop offset="0" stop-color="#c9c0a9" stop-opacity="0.55"/>
          <stop offset="1" stop-color="#c9c0a9" stop-opacity="0.85"/>
        </linearGradient>
      </defs>
      <rect x="0" y="0" width="290" height="175" rx="14" fill="url(#keyGlow)"/>
    </svg>
    <div class="brand">
      <div class="brand-name">Bright Harbor Access</div>
      <div class="brand-trade">Locksmiths</div>
    </div>
  </section>

  <section class="card card-back">
    <div class="contact">
      <div class="contact-name">Dean Rowe (<span class="korean">푸른 문지기</span>)</div>
      <div class="contact-abn">ABN 41862093715</div>
      <div class="contact-phone">ph. - 0468 219 357</div>
      <div class="contact-email">brightharboraccess@mailverte.net</div>
    </div>
    <ul class="services">
      <li>24 /7 mobile services (Including weekends &amp; public holidays)</li>
      <li>Residential / Commercial/ Automotive</li>
      <li>Opening / Repair / Installation</li>
      <li>Cut keys</li>
    </ul>
  </section>
</div>
</body>
</html>
```